Website re-design wedding music business

I need my wordpress wedding music website redesigned. I'm a wedding pianist and also provide duo/trio entertainment with other musicians and looking for an overhaul of my wordpress site.

Website: tollykessing.com.au

Target Market(s)

brides; engaged couples

Industry/Entity Type

Wedding

Number of Pages Required

5+ page

Colors

Designer to choose colors to be used in the design.

Requirements
Must have
• I'm looking to overhaul my website which is looking rather tired after 4 years. It is functional but not inviting to visitors. Initially my website started out as a solo piano player providing music for wedding. It is gradually growing now where brides can book
• 1) Solo Piano
• 2) Duo (any combination of Piano / Cello / Vocalist / Violin)
• 3) Trio (any combination of Piano/ Cello /Vocalist / Violin)
• in future it may increase to 4 / 5 /6 piece bands so that needs to be taken into account for the future growth where I'll recruit other musicians.
• Some other functionality I'd like to see
• - Visitors want a calendar to know availability of musicians
• - Automatically providing enquiry price & discount (if applicable)
• - Automating the booking form process (manual) - There's a PDF form I send to the customer after we go back/forth on email on songs/price etc but if more of it could be automated online that would be great. If move to online it would be good to be able to override the set prices with a custom price and also providing a payment gateway
• More Flexibility on pricing - customer selects type of artists they want and it calculates a price based on who they have chosen whether it is a ceremony or canapes or reception (or combination of any). Extra transport fee is added if >50km out of Melbourne.
• How would you re-design this website. Imagine you are a bride/groom looking to book wedding music services. I would love to see some concepts .
• Please indicate any other fees required for your submission and level of support post this competition. I would like this to be an on-going relationship.
Nice to have
• I'd preferably like the website to be in wordpress as I've been familiar with it over time and can do basic updates in the back end. Happy for other suggestions if you can convince me I should move away from wordpress.

```html
<!DOCTYPE html>
<html lang="en">
<head>
<meta charset="utf-8">
<title>Tolly Kessing – Wedding &amp; Event Pianist</title>
<link href="https://fonts.googleapis.com/css2?family=Montserrat:wght@400;500;600;700&family=Open+Sans:wght@400;600&display=swap" rel="stylesheet">
<style>
:root{
  --ink:#1f1f1f;
  --text:#333333;
  --muted:#8a8a8a;
  --line:#d6d6d6;
  --panel:#f3f3f3;
  --band:#e9e9e9;
  --cell:#dcdcdc;
  --cell-head:#2a2a2a;
  --dark:#222222;
  --black:#111111;
  --white:#ffffff;
}
*{box-sizing:border-box;margin:0;padding:0}
html,body{width:1200px;height:4826px;overflow:hidden;background:var(--white)}
body{font-family:"Open Sans",Arial,sans-serif;color:var(--text);position:relative}
h1,h2,h3,.nav,.btn{font-family:"Montserrat",Arial,sans-serif}
.abs{position:absolute}

/* header */
.site-header{position:absolute;left:0;top:0;width:1200px;height:183px;background:var(--white)}
.brand{position:absolute;left:130px;top:24px;width:190px;text-align:center}
.brand-mark{width:76px;height:76px;border-radius:50%;background:var(--ink);margin:0 auto 6px}
.brand-name{font-family:"Montserrat",sans-serif;font-weight:600;font-size:20px;color:var(--ink);letter-spacing:.5px;line-height:1.1}
.brand-tag{font-size:14px;color:var(--ink);margin-top:2px}
.header-book{position:absolute;left:940px;top:42px;width:128px;height:42px;border:1px solid var(--ink);font-size:12px;font-weight:600;display:flex;align-items:center;justify-content:center;gap:6px;color:var(--ink)}
.nav{position:absolute;right:132px;top:134px;display:flex;gap:32px;font-size:13px;font-weight:500;color:var(--ink);letter-spacing:.5px}
.nav .active{border-bottom:2px solid var(--ink);padding-bottom:3px}

/* hero */
.hero{position:absolute;left:0;top:183px;width:1200px;height:660px;overflow:hidden}
.hero-photo{position:absolute;inset:0;background:linear-gradient(100deg,#3b3d2a 0%,#6e7452 28%,#a8ad8c 48%,#5a6141 70%,#2d2f21 100%)}
.hero-cut{position:absolute;left:0;top:0}
.hero-cta{position:absolute;left:0;width:1200px;top:185px;text-align:center;color:var(--white)}
.hero-cta p{font-size:14px;font-weight:600}
.hero-cta h3{font-size:22px;font-weight:500;letter-spacing:1.5px;margin-top:6px}
.play{width:52px;height:52px;border-radius:50%;background:var(--white);margin:12px auto 0;display:flex;align-items:center;justify-content:center}
.arrow{position:absolute;font-size:30px;color:#bbbbbb;font-family:"Montserrat",sans-serif}

.section-title{position:absolute;left:0;width:1200px;text-align:center;font-family:"Montserrat",sans-serif;font-weight:500;font-size:42px;color:var(--ink)}

/* welcome */
.welcome-text{position:absolute;left:132px;top:893px;width:455px;font-size:17px;line-height:1.5;color:var(--ink)}
.badges{position:absolute;left:138px;top:1025px;display:flex;gap:34px}
.badge{width:130px;height:130px;border-radius:50%}
.welcome-photo{position:absolute;left:633px;top:883px;width:435px;height:290px;background:linear-gradient(160deg,#6e7a4c,#39402a 60%,#d7d7d2 85%)}

/* pricing */
.price-card{position:absolute;top:1496px;width:302px;height:376px;background:var(--white);box-shadow:0 4px 14px rgba(0,0,0,.15);text-align:center;padding-top:40px}
.price-card h3{font-size:28px;font-weight:500;color:var(--ink)}
.price-card .sub{font-size:13px;color:var(--text);line-height:1.4;margin-top:6px;min-height:36px}
.price-tag{width:176px;height:60px;margin:22px auto 0;background:#eeeeee;font-family:"Montserrat",sans-serif;font-size:30px;display:flex;align-items:center;justify-content:center;color:var(--ink)}
.price-card .blurb{font-size:10px;color:var(--muted);line-height:1.55;width:230px;margin:28px auto 0}
.btn{display:inline-flex;align-items:center;gap:6px;border:1px solid var(--ink);font-size:11px;font-weight:600;padding:0 18px;height:36px;margin-top:26px;color:var(--ink)}

/* calendar */
.calendar{position:absolute;left:132px;top:2245px;width:936px;border-collapse:collapse;table-layout:fixed;font-family:"Montserrat",sans-serif}
.cal-bar{background:var(--cell-head);color:var(--white);height:45px;font-size:20px;text-align:center}
.cal-bar td{position:relative}
.cal-days th{background:var(--black);color:var(--white);height:50px;font-size:16px;font-weight:500}
.calendar td.day{background:var(--cell);height:97px;border:2px solid var(--white);text-align:center;vertical-align:middle;font-size:30px;color:var(--ink);position:relative}
.calendar td.out{color:#a8a8a8;background:#e4e4e4}
.calendar td.out{background-image:linear-gradient(to top left,#ececec 50%,#e1e1e1 50%)}
.day small{display:block;font-family:"Open Sans",sans-serif;font-size:12px;color:var(--ink);margin-top:2px}
.out small{color:#9a9a9a}

/* offer */
.offer{position:absolute;left:0;top:2935px;width:1200px;height:655px;overflow:hidden}
.offer-photo{position:absolute;left:598px;top:0;width:602px;height:655px;background:linear-gradient(120deg,#4a4a3a,#6a5c43 40%,#8a5230 60%,#2f2b22)}
.offer-text{position:absolute;left:132px;top:300px;width:420px;color:var(--white)}
.offer-text h2{font-size:42px;font-weight:500}
.offer-text h3{font-size:44px;font-weight:600;color:#cfcfcf;margin-top:2px;letter-spacing:1px}
.offer-text h3 sup{font-size:24px}
.offer-text p{font-size:13px;line-height:1.5;margin-top:10px}
.btn-light{border-color:#aaaaaa;color:var(--white);margin-top:18px;height:34px}

/* testimonials */
.quote{position:absolute;left:132px;top:3728px;width:936px;text-align:center;font-size:17px;line-height:1.65;color:var(--ink)}
.quote cite{display:block;font-style:normal;font-weight:600;margin-top:14px}

/* booking form */
.form-lead{position:absolute;left:0;width:1200px;top:4188px;text-align:center;font-size:13px;color:var(--ink)}
.checks{position:absolute;left:132px;top:4222px;width:936px;display:flex;justify-content:space-between;font-size:12px;color:var(--text)}
.checks label{display:flex;gap:6px;align-items:flex-start;width:108px;line-height:1.3}
.checks i{width:13px;height:13px;border:1px solid #999;flex:none;margin-top:2px}
.field{position:absolute;height:42px;border:1px solid var(--line);font-size:11px;color:#777;padding:0 12px;display:flex;align-items:center;justify-content:space-between}
.submit{position:absolute;left:552px;top:4472px;width:98px;height:40px;background:var(--black);color:var(--white);font-family:"Montserrat",sans-serif;font-size:12px;font-weight:600;display:flex;align-items:center;justify-content:center}
.note{position:absolute;left:0;width:1200px;top:4528px;text-align:center;font-size:11px;color:#666}

/* footer */
.site-footer{position:absolute;left:0;top:4626px;width:1200px;height:200px;background:var(--black);color:#cccccc;text-align:center}
.footer-nav{margin-top:48px;font-size:12px}
.footer-nav span{margin:0 6px}
.copy{font-size:11px;margin-top:10px;color:#999}
.social{display:flex;justify-content:center;gap:14px;margin-top:20px}
.social i{width:38px;height:38px;border-radius:50%;border:1px solid #666}
</style>
</head>
<body>

<header class="site-header">
  <div class="brand">
    <div class="brand-mark"></div>
    <div class="brand-name">TOLLY KESSING</div>
    <div class="brand-tag">Wedding &amp; Event Pianist</div>
  </div>
  <div class="header-book">
    <svg width="12" height="12" viewBox="0 0 12 12"><rect x="1" y="1" width="10" height="10" fill="none" stroke="#1f1f1f"/><path d="M4 8l5-5" stroke="#1f1f1f"/></svg>BOOK NOW
  </div>
  <nav class="nav">
    <span class="active">HOME</span><span>ABOUT</span><span>SERVICES</span><span>PRICES</span><span>EVENT</span><span>GALLERY</span><span>CONTACT</span><span>MORE ▾</span>
  </nav>
</header>

<section class="hero">
  <div class="hero-photo" role="img" aria-label="Pianist at a white grand piano and a cellist playing outdoors under trees"></div>
  <svg class="hero-cut" width="1200" height="660"><polygon points="1200,420 1200,660 560,660" fill="#ffffff"/><polygon points="0,610 560,660 0,660" fill="#ffffff"/></svg>
  <div class="hero-cta">
    <p>Click here to hear our music</p>
    <h3>LANTERNS – EVENING TIDE</h3>
    <div class="play"><svg width="20" height="22" viewBox="0 0 20 22"><polygon points="3,1 19,11 3,21" fill="#1f1f1f"/></svg></div>
  </div>
  <div class="arrow" style="left:24px;top:245px">‹</div>
  <div class="arrow" style="right:24px;top:245px">›</div>
</section>

<h2 class="section-title" style="top:790px">Welcome</h2>
<p class="welcome-text">Tolly Kessing is Melbourne's premier award wedding &amp; event pianist specialising in playing beautiful background music for weddings, special occasions &amp; corporate events.</p>
<div class="badges">
  <div class="badge" style="background:#2a2a2a"></div>
  <div class="badge" style="background:#b8902e"></div>
  <div class="badge" style="background:#9a9cb8"></div>
</div>
<div class="welcome-photo" role="img" aria-label="Pianist seated at a white grand piano in a park"></div>

<svg class="abs" style="left:0;top:1190px" width="1200" height="1000">
  <polygon points="0,0 1200,160 1200,1000 0,1000" fill="#f3f3f3"/>
  <polygon points="0,0 700,130 0,245" fill="#e4e4e4"/>
  <polygon points="1200,720 1200,1000 0,1000" fill="#ffffff"/>
</svg>

<h2 class="section-title" style="top:1398px">Pricing</h2>
<div class="arrow" style="left:34px;top:1658px">‹</div>
<div class="arrow" style="right:34px;top:1658px">›</div>

<div class="price-card" style="left:132px">
  <h3>Solo Piano</h3><p class="sub">&nbsp;</p>
  <div class="price-tag">$00.00</div>
  <p class="blurb">Gentle piano melodies for your ceremony, canapes and reception, tailored to the songs you love most.</p>
  <span class="btn">✎ BOOK NOW</span>
</div>
<div class="price-card" style="left:450px">
  <h3>Duo</h3><p class="sub">any combination of<br>Piano / Cello / Vocalist / Violin</p>
  <div class="price-tag">$00.00</div>
  <p class="blurb">Two musicians blending warm sound for your special day, from the aisle walk to the final dance.</p>
  <span class="btn">✎ BOOK NOW</span>
</div>
<div class="price-card" style="left:766px">
  <h3>Trio</h3><p class="sub">any combination of<br>Piano / Cello / Vocalist / Violin</p>
  <div class="price-tag">$00.00</div>
  <p class="blurb">A fuller ensemble with rich layered music for larger venues, guests and celebrations of every size.</p>
  <span class="btn">✎ BOOK NOW</span>
</div>

<h2 class="section-title" style="top:2162px">Check our availability</h2>
<table class="calendar">
  <tr class="cal-bar"><td colspan="7"><span style="position:absolute;left:50px">‹</span>JULY - 2017<span style="position:absolute;right:50px">›</span></td></tr>
  <tr class="cal-days"><th>SUN</th><th>MON</th><th>TUE</th><th>WED</th><th>THU</th><th>FRI</th><th>SAT</th></tr>
  <tr><td class="day out">25</td><td class="day out">26</td><td class="day out">27</td><td class="day out">28<small>Booked</small></td><td class="day out">29</td><td class="day out">30</td><td class="day">1<small>Booked</small></td></tr>
  <tr><td class="day">2</td><td class="day">3</td><td class="day">4<small>Booked</small></td><td class="day">5</td><td class="day">6</td><td class="day">7<small>Booked</small></td><td class="day">8</td></tr>
  <tr><td class="day">9</td><td class="day">10</td><td class="day">11</td><td class="day">12</td><td class="day">13<small>Booked</small></td><td class="day">14</td><td class="day">15</td></tr>
  <tr><td class="day">16</td><td class="day">17<small>Booked</small></td><td class="day">18</td><td class="day">19</td><td class="day">20</td><td class="day">21</td><td class="day">22</td></tr>
  <tr><td class="day">23</td><td class="day">24</td><td class="day">25</td><td class="day">26<small>Booked</small></td><td class="day">27<small>Booked</small></td><td class="day">28</td><td class="day">29</td></tr>
  <tr><td class="day">30</td><td class="day">31<small>Booked</small></td><td class="day out">1</td><td class="day out">2</td><td class="day out">3</td><td class="day out">4<small>Booked</small></td><td class="day out">5</td></tr>
</table>

<section class="offer">
  <svg class="abs" style="left:0;top:0" width="1200" height="655"><polygon points="0,230 598,70 598,655 0,655" fill="#222222"/></svg>
  <div class="offer-photo" role="img" aria-label="Cellist playing a cello outdoors among trees"></div>
  <svg class="abs" style="left:598px;top:0" width="602" height="80"><polygon points="0,0 602,0 0,70" fill="#ffffff"/></svg>
  <div class="offer-text">
    <h2>Special Offer</h2>
    <h3>JULY 6<sup>TH</sup> TO 18<sup>TH</sup></h3>
    <p>any combination of Piano / Cello / Vocalist / Violin<br>Mauris suscipit felis id nunc elementum varius. Praesent elementum nulla sit amet justo pellentesque scelerisque. Nam et tortor in ante iaculis porttitor in luctus mi.</p>
    <span class="btn btn-light">✎ BOOK NOW</span>
  </div>
</section>

<h2 class="section-title" style="top:3652px">Testimonials</h2>
<div class="arrow" style="left:34px;top:3775px">‹</div>
<div class="arrow" style="right:34px;top:3775px">›</div>
<blockquote class="quote">" Tolly played at our ceremony at Harbourlight, Eastbank on the 30th October 2016. His music was beautiful and absolutely perfect for the occasion. He even went so far as to learn a specific song to play while we were walking down the isle. I couldn't be happier with the result – a smooth, sophisticated and perfect result. Do yourself a favour and leave the music to Tolly – he will make sure that your wedding is perfect too. "<cite>- Rosalind and Theo</cite></blockquote>

<svg class="abs" style="left:0;top:3920px" width="1200" height="210"><polygon points="1200,0 1200,90 0,210 0,130" fill="#f0f0f0"/></svg>

<h2 class="section-title" style="top:4118px">Book Now</h2>
<p class="form-lead">What are you interested in?</p>
<div class="checks">
  <label><i></i>Ceremony</label><label><i></i>Canapés</label><label><i></i>Reception</label><label><i></i>Live Performance</label><label><i></i>Accompaniment</label><label><i></i>Recorded Material</label><label><i></i>Hire Baby Grand Piano (Std)</label><label style="width:60px"><i></i>Other</label>
</div>
<div class="field" style="left:132px;top:4280px;width:218px">Name*</div>
<div class="field" style="left:372px;top:4280px;width:218px">Email*</div>
<div class="field" style="left:612px;top:4280px;width:218px">Phone number*</div>
<div class="field" style="left:850px;top:4280px;width:218px">Date of Occasion*<span>▦</span></div>
<div class="field" style="left:132px;top:4343px;width:218px">Time / Hours Required*<span>◷</span></div>
<div class="field" style="left:372px;top:4343px;width:218px">Location*<span>⌖</span></div>
<div class="field" style="left:612px;top:4343px;width:218px">Subject</div>
<div class="field" style="left:850px;top:4343px;width:218px">How did you find us?<span>▾</span></div>
<div class="field" style="left:132px;top:4407px;width:936px">Message</div>
<div class="submit">SUBMIT</div>
<p class="note">Extra transport fee is added if &gt;50km out of Melbourne</p>

<footer class="site-footer">
  <div class="footer-nav"><span>Home</span>|<span>About</span>|<span>Services</span>|<span>Prices</span>|<span>Event</span>|<span>Gallery</span>|<span>Contact</span>|<span>More</span></div>
  <p class="copy">Copyright © 2017 · Tolly Kessing · All rights reserved.</p>
  <div class="social"><i></i><i></i><i></i><i></i></div>
</footer>

</body>
</html>
```